Renew plant-based protein powder label

I would like a redesign for my current protein powder label . The current label idea should not be altered too much, but the design should be taken to the next level. Keep in mind that is should remain professional, not too extravagant. The main color for this label should remain red, because I represent each of my products with a specific color. It would be nice if a subtle (green) touch could be implemented to represent the plant based protein.

The logo should not be altered, and I prefer designs in Adobe Indesign (so I can adjust minor things if necessary later on).
Updates

Some adjustments to my project description: I generally like the idea of my current label but think that it can be uplifted even more. For instance, I like the idea of the hexagon structures as it is now, but it can be done better (try to create a 'wow-effect'). This does not mean that I exclude any other ideas, but they should be really good as otherwise it does not make any sense switching my entire product line to the new label format. The leaf picture that I included is not mandatory to use (as I have seen this a lot). I think the way in which Design #51394062 presented the bottom information (nr. of doses etc.) is creative. But as I mentioned, I intend to adjust the whole product line to this format so it has to be really good. Thanks a lot for your efforts and I look forward to new creativity.

Target Market(s)

Fitness market. usual customer is aged 18-25.

Industry/Entity Type

Fitness. Weight lifting.

Other font styles liked:
• See fonts attached that I use now. Use no script fonts.

Colors
00AB8E
00BBA5
67D7C9
C6EFE9
E9F9F6
EB3D1F
EC4F4E
F09395
F8D3D4
FCEDEE

Requirements
Must have
• The current design idea implemented.
Nice to have
• A subtle, but creative element of the plant-based aspect. Try to keep the main color red.
Should not have
• Extravagant designs

```html
<!DOCTYPE html>
<html lang="en">
<head>
<meta charset="utf-8">
<title>Granite Nutrition – Pure Cacao Plant Protein Label</title>
<link rel="stylesheet" href="https://fonts.googleapis.com/css2?family=Montserrat:wght@400;500;600;700;800&display=swap">
<style>
  :root {
    --teal-deep: #00AB8E;
    --teal: #00BBA5;
    --teal-light: #67D7C9;
    --teal-pale: #C6EFE9;
    --teal-mist: #E9F9F6;
    --red-deep: #EB3D1F;
    --red: #EC4F4E;
    --red-soft: #F09395;
    --red-pale: #F8D3D4;
    --red-mist: #FCEDEE;
    --backdrop: #7DD3CA;
    --white: #FFFFFF;
    --ink: #3A3A3A;
  }
  * { box-sizing: border-box; margin: 0; padding: 0; }
  html, body { width: 800px; height: 1200px; overflow: hidden; }
  body {
    background: var(--backdrop);
    font-family: 'Montserrat', sans-serif;
    position: relative;
  }

  /* ---------- Front panel ---------- */
  .front {
    position: absolute;
    width: 600px;
    height: 460px;
    overflow: hidden;
  }
  .front--hero { left: 100px; top: 110px; box-shadow: 0 10px 30px rgba(0,0,0,.12); }
  .front__top-band {
    position: absolute; left: 0; top: 0; width: 100%; height: 22px;
    background: var(--teal-deep);
  }
  .front__red {
    position: absolute; left: 0; top: 22px; width: 100%; height: 268px;
    background: linear-gradient(135deg, var(--red) 0%, var(--red-deep) 100%);
  }
  .front__texture {
    position: absolute; inset: 0;
    background: radial-gradient(ellipse at 20% 30%, rgba(255,255,255,.10), transparent 60%),
                radial-gradient(ellipse at 85% 70%, rgba(255,255,255,.08), transparent 55%);
  }
  .brand {
    position: absolute; left: 50%; top: 0; transform: translateX(-50%);
    width: 236px; height: 112px;
    background: var(--teal);
    border: 3px solid var(--white);
    border-top: none;
    display: flex; align-items: center; justify-content: center; gap: 10px;
  }
  .brand__dot {
    width: 16px; height: 16px; border-radius: 50%;
    background: var(--white);
  }
  .brand__name {
    color: var(--white);
    font-weight: 600;
    font-size: 19px;
    letter-spacing: 1.5px;
    text-transform: uppercase;
    line-height: 1.15;
  }
  .product-name {
    position: absolute; left: 0; right: 0; top: 150px;
    text-align: center;
    color: var(--white);
    font-size: 66px;
    letter-spacing: 1px;
    line-height: 1;
  }
  .product-name__bold { font-weight: 800; }
  .product-name__light { font-weight: 500; }
  .front__teal {
    position: absolute; left: 0; top: 290px; width: 100%; height: 150px;
    background: var(--teal-deep);
  }
  .protein-type {
    position: absolute; left: 50%; top: 20px; transform: translateX(-50%);
    width: 380px; height: 58px;
    background: var(--teal-light);
    border: 2px solid var(--white);
    display: flex; align-items: center; justify-content: center;
    color: var(--white);
    font-weight: 600; font-size: 30px; letter-spacing: 1px;
  }
  .pack-info {
    position: absolute; left: 50%; top: 96px; transform: translateX(-50%);
    width: 380px; height: 30px;
    display: flex;
    border-top: 1px solid rgba(255,255,255,.7);
    border-bottom: 1px solid rgba(255,255,255,.7);
  }
  .pack-info__item {
    flex: 1; display: flex; align-items: center; justify-content: center;
    color: var(--white); font-size: 14px; font-weight: 500;
  }
  .pack-info__item + .pack-info__item { border-left: 1px solid rgba(255,255,255,.7); }
  .front__bottom-band {
    position: absolute; left: 0; top: 440px; width: 100%; height: 20px;
    background: var(--red-deep);
  }

  /* ---------- Full wrap label ---------- */
  .wrap-label {
    position: absolute; left: 20px; top: 700px;
    width: 760px; height: 292px;
    background: linear-gradient(135deg, var(--red) 0%, var(--red-deep) 100%);
    overflow: hidden;
    box-shadow: 0 10px 30px rgba(0,0,0,.12);
  }
  .wrap-label__top-band {
    position: absolute; left: 0; top: 0; width: 100%; height: 14px;
    background: var(--teal-deep);
  }
  .wrap-label__bottom-band {
    position: absolute; left: 0; bottom: 0; width: 100%; height: 13px;
    background: var(--red-deep);
  }
  .front--mini {
    left: 190px; top: 0;
    transform: scale(0.6333);
    transform-origin: 0 0;
  }
  .side-panel {
    position: absolute; top: 24px; width: 172px; height: 244px;
    background: var(--white);
    padding: 8px 9px;
    color: var(--ink);
    font-size: 5.4px;
    line-height: 1.45;
  }
  .side-panel--info { left: 9px; }
  .side-panel--facts { right: 9px; }
  .side-panel__heading {
    display: inline-block;
    background: var(--red);
    color: var(--white);
    font-weight: 700;
    font-size: 5.8px;
    text-transform: uppercase;
    letter-spacing: .4px;
    padding: 1px 4px;
    margin: 5px 0 3px;
  }
  .side-panel__heading:first-child { margin-top: 0; }
  .side-panel__text { margin-bottom: 3px; }
  .facts-table { width: 100%; border-collapse: collapse; font-size: 5.4px; }
  .facts-table th {
    text-align: left; font-weight: 700;
    border-bottom: 1px solid var(--ink);
    padding: 2px 0;
  }
  .facts-table td { padding: 1.6px 0; border-bottom: .5px solid var(--teal-pale); }
  .facts-table td:not(:first-child), .facts-table th:not(:first-child) { text-align: right; }
  .facts-table .facts-table__key td { font-weight: 700; color: var(--teal-deep); }
  .side-panel__note { margin-top: 8px; color: var(--teal-deep); font-weight: 600; }
</style>
</head>
<body>

  <!-- Front panel -->
  <section class="front front--hero">
    <div class="front__top-band"></div>
    <div class="front__red">
      <div class="front__texture"></div>
      <div class="brand">
        <span class="brand__dot"></span>
        <span class="brand__name">Granite<br>Nutrition</span>
      </div>
      <h1 class="product-name"><span class="product-name__bold">PURE</span> <span class="product-name__light">CACAO</span></h1>
    </div>
    <div class="front__teal">
      <div class="protein-type">PLANT PROTEIN</div>
      <div class="pack-info">
        <span class="pack-info__item">33 Servings</span>
        <span class="pack-info__item">1,000 Gram</span>
      </div>
    </div>
    <div class="front__bottom-band"></div>
  </section>

  <!-- Full wrap-around label -->
  <section class="wrap-label">
    <div class="wrap-label__top-band"></div>

    <div class="side-panel side-panel--info">
      <h2 class="side-panel__heading">Product information</h2>
      <p class="side-panel__text">A smooth plant protein blend of pea and rice with real cacao. Vegan, soy free and low in sugar.</p>
      <h2 class="side-panel__heading">Directions</h2>
      <p class="side-panel__text">Mix one scoop with 300 ml water or plant milk. Shake well and enjoy after training.</p>
      <h2 class="side-panel__heading">Ingredients</h2>
      <p class="side-panel__text">Pea protein isolate, rice protein, cacao powder, natural flavour, stevia.</p>
    </div>

    <section class="front front--mini">
      <div class="front__top-band"></div>
      <div class="front__red">
        <div class="front__texture"></div>
        <div class="brand">
          <span class="brand__dot"></span>
          <span class="brand__name">Granite<br>Nutrition</span>
        </div>
        <h2 class="product-name"><span class="product-name__bold">PURE</span> <span class="product-name__light">CACAO</span></h2>
      </div>
      <div class="front__teal">
        <div class="protein-type">PLANT PROTEIN</div>
        <div class="pack-info">
          <span class="pack-info__item">33 Servings</span>
          <span class="pack-info__item">1,000 Gram</span>
        </div>
      </div>
      <div class="front__bottom-band"></div>
    </section>

    <div class="side-panel side-panel--facts">
      <h2 class="side-panel__heading">Nutrition facts</h2>
      <table class="facts-table">
        <tr><th>Nutrient</th><th>per 100 g</th><th>per 30 g</th></tr>
        <tr><td>Energy</td><td>1580 kJ</td><td>474 kJ</td></tr>
        <tr><td>Fat</td><td>6.2 g</td><td>1.9 g</td></tr>
        <tr><td>Saturates</td><td>1.4 g</td><td>0.4 g</td></tr>
        <tr><td>Carbohydrates</td><td>5.8 g</td><td>1.7 g</td></tr>
        <tr><td>Sugars</td><td>1.1 g</td><td>0.3 g</td></tr>
        <tr><td>Fibre</td><td>4.5 g</td><td>1.4 g</td></tr>
        <tr class="facts-table__key"><td>Protein</td><td>74 g</td><td>22 g</td></tr>
        <tr><td>Salt</td><td>1.2 g</td><td>0.4 g</td></tr>
      </table>
      <p class="side-panel__note">Store in a cool, dry place.</p>
    </div>

    <div class="wrap-label__bottom-band"></div>
  </section>

</body>
</html>
```